Need modern simple design for magazine ad, apartment and condo roofer.

I need a half page magazine ad for a local roofer to publish in an industry magazine. Apartment associations industry. All types of roofs. Shingle and Flat
Need the design to be creative and modern, clean and simple. I do not want a busy design. One that stands out and makes a point quickly.
Logo must be prominent.
DO NOT USE PHOTOS FROM MY WEBSITE PLEASE. Looking for something new.
I work on entire complexes not houses.

Need to make sure our phone number and email address are listed at the bottom. Here is my website www.vorbelan.com
Want to stay away from standard clip arts of tools, homes, apartment buildings.
Half Horizontal 7.25 x 4.75
Ads should be in PDF and JPG format.

Target Market(s)

Apartment or Condo owners looking for large scale roofing projects

Industry/Entity Type

Roofing

Requirements
Must have
• Prominent Logo
Simple Clean Design
Create graphics
Not Busy
Should not have
• Clip Art
No Photos from my website

```html
<!DOCTYPE html>
<html lang="en">
<head>
<meta charset="utf-8">
<title>Vorbelan Roofing – Half Page Ad</title>
<link rel="stylesheet" href="https://fonts.googleapis.com/css2?family=Montserrat:wght@400;700;800&display=swap">
<style>
  :root {
    --page-bg: #c4c4c4;
    --paper: #ffffff;
    --brand-blue: #1a74c4;
    --brand-blue-light: #3a9de6;
    --accent-blue: #2a8de0;
    --tick-blue: #1d78c8;
    --body-text: #3a3a3a;
    --footer-dark: #2b2b2b;
    --footer-mid: #474747;
    --amp-grey: #8e8e8e;
    --brand-grey: #7d7d7d;
  }
  * { box-sizing: border-box; margin: 0; padding: 0; }
  html, body { width: 1200px; height: 1200px; overflow: hidden; }
  body { background: var(--page-bg); font-family: "Montserrat", sans-serif; position: relative; }

  .ad {
    position: absolute; left: 40px; top: 233px;
    width: 1120px; height: 734px;
    background: var(--paper); overflow: hidden;
  }
  .brand {
    position: absolute; left: 44px; top: 40px;
    display: flex; align-items: center; gap: 16px;
  }
  .brand-square { width: 58px; height: 58px; background: var(--brand-blue); }
  .brand-name {
    font-weight: 800; font-size: 46px; color: var(--brand-grey);
    letter-spacing: -0.5px; line-height: 1;
  }

  .headline-band {
    position: absolute; left: 0; top: 155px; width: 536px; height: 222px;
    background: linear-gradient(180deg, var(--brand-blue-light) 0%, var(--brand-blue) 45%, var(--brand-blue) 100%);
    border-top: 4px solid #1767b0;
    color: #fff; padding: 26px 0 0 42px;
  }
  .headline-kicker { font-weight: 700; font-size: 19px; letter-spacing: 1px; }
  .headline-line { font-weight: 800; line-height: 1.08; }
  .headline-line.mid { font-size: 33px; margin-top: 10px; }
  .headline-line.big { font-size: 45px; display: flex; align-items: center; gap: 6px; }
  .amp-box {
    display: inline-flex; align-items: center; justify-content: center;
    width: 64px; height: 54px; background: var(--amp-grey); border-radius: 8px; font-size: 40px;
  }

  .services {
    position: absolute; left: 44px; top: 410px;
    display: grid; grid-template-columns: 245px 240px; column-gap: 0;
  }
  .service-list { list-style: none; }
  .service-list li {
    display: flex; align-items: flex-start; gap: 6px;
    font-size: 15px; color: var(--body-text); line-height: 22.7px;
  }
  .tick { flex: none; width: 11px; height: 11px; margin-top: 5px; }

  .footer-shape { position: absolute; left: 0; top: 616px; width: 640px; height: 118px; }
  .footer-content { position: absolute; left: 44px; top: 640px; color: #fff; }
  .call-line { font-weight: 800; font-size: 31px; letter-spacing: 0.3px; }
  .call-line .phone { color: var(--accent-blue); }
  .contact-row { display: flex; gap: 18px; margin-top: 14px; font-size: 16px; letter-spacing: 0.4px; }
  .contact-item { display: flex; align-items: center; gap: 8px; }
  .contact-icon { width: 26px; height: 26px; background: var(--accent-blue); border-radius: 3px; display: flex; align-items: center; justify-content: center; }

  .photo {
    position: absolute; left: 545px; top: 0; width: 575px; height: 734px;
    background: linear-gradient(180deg, #8fb8e8 0%, #b9774f 30%, #a8613f 60%, #d09030 78%, #5f7f3a 90%, #7d9a4a 100%);
  }
</style>
</head>
<body>
  <main class="ad">
    <div class="photo" role="img" aria-label="Photo of a modern brick apartment building with glass balconies above a landscaped garden of orange flowers"></div>

    <header class="brand">
      <span class="brand-square"></span>
      <span class="brand-name">Vorbelan Roofing</span>
    </header>

    <section class="headline-band">
      <p class="headline-kicker">IMPROVING AND ADDING VALUE TO</p>
      <p class="headline-line mid">MULTIFAMILY APARTMENT</p>
      <p class="headline-line big">COMMUNITIES <span class="amp-box">&amp;</span></p>
      <p class="headline-line big">STUDENT HOUSING</p>
    </section>

    <section class="services">
      <ul class="service-list">
        <li><svg class="tick" viewBox="0 0 12 12"><circle cx="6" cy="6" r="6" fill="#1d78c8"/><path d="M3.2 6.2l1.9 1.8 3.7-3.8" stroke="#fff" stroke-width="1.6" fill="none"/></svg>Fire Restoration</li>
        <li><svg class="tick" viewBox="0 0 12 12"><circle cx="6" cy="6" r="6" fill="#1d78c8"/><path d="M3.2 6.2l1.9 1.8 3.7-3.8" stroke="#fff" stroke-width="1.6" fill="none"/></svg>Due Diligence</li>
        <li><svg class="tick" viewBox="0 0 12 12"><circle cx="6" cy="6" r="6" fill="#1d78c8"/><path d="M3.2 6.2l1.9 1.8 3.7-3.8" stroke="#fff" stroke-width="1.6" fill="none"/></svg>Exterior Renovations</li>
        <li><svg class="tick" viewBox="0 0 12 12"><circle cx="6" cy="6" r="6" fill="#1d78c8"/><path d="M3.2 6.2l1.9 1.8 3.7-3.8" stroke="#fff" stroke-width="1.6" fill="none"/></svg>Siding / Wood Replacement</li>
        <li><svg class="tick" viewBox="0 0 12 12"><circle cx="6" cy="6" r="6" fill="#1d78c8"/><path d="M3.2 6.2l1.9 1.8 3.7-3.8" stroke="#fff" stroke-width="1.6" fill="none"/></svg>Full Paint</li>
        <li><svg class="tick" viewBox="0 0 12 12"><circle cx="6" cy="6" r="6" fill="#1d78c8"/><path d="M3.2 6.2l1.9 1.8 3.7-3.8" stroke="#fff" stroke-width="1.6" fill="none"/></svg>Roofing (all types)</li>
        <li><svg class="tick" viewBox="0 0 12 12"><circle cx="6" cy="6" r="6" fill="#1d78c8"/><path d="M3.2 6.2l1.9 1.8 3.7-3.8" stroke="#fff" stroke-width="1.6" fill="none"/></svg>Balcony/Landing Repairs</li>
      </ul>
      <ul class="service-list">
        <li><svg class="tick" viewBox="0 0 12 12"><circle cx="6" cy="6" r="6" fill="#1d78c8"/><path d="M3.2 6.2l1.9 1.8 3.7-3.8" stroke="#fff" stroke-width="1.6" fill="none"/></svg>Concrete</li>
        <li><svg class="tick" viewBox="0 0 12 12"><circle cx="6" cy="6" r="6" fill="#1d78c8"/><path d="M3.2 6.2l1.9 1.8 3.7-3.8" stroke="#fff" stroke-width="1.6" fill="none"/></svg>Brick/Stucco/Masonry</li>
        <li><svg class="tick" viewBox="0 0 12 12"><circle cx="6" cy="6" r="6" fill="#1d78c8"/><path d="M3.2 6.2l1.9 1.8 3.7-3.8" stroke="#fff" stroke-width="1.6" fill="none"/></svg>Carports / Metal Fencing</li>
        <li><svg class="tick" viewBox="0 0 12 12"><circle cx="6" cy="6" r="6" fill="#1d78c8"/><path d="M3.2 6.2l1.9 1.8 3.7-3.8" stroke="#fff" stroke-width="1.6" fill="none"/></svg>Disaster Restoration</li>
        <li><svg class="tick" viewBox="0 0 12 12"><circle cx="6" cy="6" r="6" fill="#1d78c8"/><path d="M3.2 6.2l1.9 1.8 3.7-3.8" stroke="#fff" stroke-width="1.6" fill="none"/></svg>Interior Renovations</li>
        <li><svg class="tick" viewBox="0 0 12 12"><circle cx="6" cy="6" r="6" fill="#1d78c8"/><path d="M3.2 6.2l1.9 1.8 3.7-3.8" stroke="#fff" stroke-width="1.6" fill="none"/></svg><span>Leasing Office Renovations<br>and more</span></li>
      </ul>
    </section>

    <svg class="footer-shape" viewBox="0 0 640 118" preserveAspectRatio="none" aria-hidden="true">
      <defs>
        <linearGradient id="footerFill" x1="0" y1="0" x2="0" y2="1">
          <stop offset="0" stop-color="#474747"/>
          <stop offset="1" stop-color="#2b2b2b"/>
        </linearGradient>
      </defs>
      <polygon points="0,0 524,0 640,118 0,118" fill="#ffffff"/>
      <polygon points="0,0 516,0 620,118 0,118" fill="url(#footerFill)"/>
    </svg>

    <footer class="footer-content">
      <p class="call-line">CALL US NOW <span class="phone">817.555.0148</span></p>
      <div class="contact-row">
        <span class="contact-item">
          <span class="contact-icon"><svg width="18" height="13" viewBox="0 0 18 13"><rect x="0.8" y="0.8" width="16.4" height="11.4" fill="none" stroke="#fff" stroke-width="1.5"/><path d="M1 1l8 6 8-6M1 12l6-5M17 12l-6-5" stroke="#fff" stroke-width="1.3" fill="none"/></svg></span>
          info@vorbelan.com
        </span>
        <span class="contact-item">
          <span class="contact-icon"><svg width="18" height="18" viewBox="0 0 18 18"><circle cx="9" cy="9" r="7.5" fill="none" stroke="#fff" stroke-width="1.4"/><ellipse cx="9" cy="9" rx="3.4" ry="7.5" fill="none" stroke="#fff" stroke-width="1.2"/><path d="M1.5 9h15M3 5h12M3 13h12" stroke="#fff" stroke-width="1.1"/></svg></span>
          www.vorbelan.com
        </span>
      </div>
    </footer>
  </main>
</body>
</html>
```